Current website re-design to a updated look and feel.

We currently have a website www.brightlanefreight.com that we want to give an updated look and feel to. We are a logistics company that competes with Falcora, Dw Hartley, Vanta but on a smaller scale. We want something fresh and updated. We have two locations one in downtown Chicago, IL and one in Palatine IL. We are a fun group that also gets the job done. We know we need pictures of both locations and possibly a video, but we need fresh design ideas. The 'who we are' page is really the only page that we currently want to keep. The 'what we do' page needs to be completely re-done from a look and feel for sure.

Target Market(s)

Anyone who uses Truck transportation to move their product. Mainly US manufacturers.

Industry/Entity Type

Logistics

Number of Pages Required

5+ page

Font styles to use
Sans Serif

Colors
5c91c4
0355a3
d0dfed

Requirements
Must have
• The new design must entice people to want to do business with us. The design must have locations for pictures and at least one video which we know we will have to provide. Design must be easy to navigate.

```html
<!DOCTYPE html>
<html lang="en">
<head>
<meta charset="utf-8">
<title>Brightlane Freight</title>
<link href="https://fonts.googleapis.com/css2?family=Open+Sans:wght@300;400;600;700&display=swap" rel="stylesheet">
<style>
:root{
  --navy:#0a3c7d;
  --brand:#0355a3;
  --sky:#5c91c4;
  --mist:#d0dfed;
  --bright:#1474d4;
  --green:#8cc63f;
  --ink:#333333;
  --muted:#666666;
  --dark:#2a2a2a;
  --black:#111111;
  --white:#ffffff;
}
*{box-sizing:border-box;margin:0;padding:0}
html,body{width:1200px;height:3629px;overflow:hidden}
body{font-family:"Open Sans",Arial,sans-serif;color:var(--ink);background:var(--white);position:relative}
.abs{position:absolute}
.topbar{top:0;left:0;width:1200px;height:44px;background:var(--navy);color:var(--white);font-size:14px}
.topbar .contact{left:80px;top:13px;display:flex;gap:26px;align-items:center}
.topbar .contact span{display:flex;gap:7px;align-items:center}
.topbar .social{left:912px;top:15px;display:flex;gap:14px}
.dot{width:12px;height:12px;border-radius:50%;background:var(--white);opacity:.85}
.topbar .login{left:1052px;top:9px;width:72px;height:26px;background:var(--sky);color:var(--white);font-size:13px;text-align:center;line-height:26px}
.header{top:44px;left:0;width:1200px;height:89px;background:var(--white)}
.logo{left:70px;top:22px;display:flex;align-items:center;gap:10px;font-size:30px;font-weight:600;color:var(--brand)}
.logo i{width:16px;height:16px;background:var(--brand);border-radius:50%;display:block}
.nav{right:68px;top:38px;display:flex;gap:44px;font-size:14px;color:#444;letter-spacing:.3px}
.hero{top:133px;left:0;width:1200px;height:598px;background:linear-gradient(180deg,#b8c6d6 0%,#8293a6 35%,#4e5a66 60%,#6b4a40 85%,#3a3f4a 100%)}
.title{width:1200px;left:0;text-align:center;font-size:31px;font-weight:400;letter-spacing:1px;color:#222}
.divider{left:570px;width:60px;height:10px}
.founder-photo{left:102px;top:832px;width:232px;height:232px;border-radius:50%;border:2px solid #ddd;background:linear-gradient(160deg,#e9e5dd,#a8a089 60%,#6f6b55)}
.founder-text{left:397px;top:838px;width:730px;font-size:14.5px;line-height:24px;color:#444}
.founder-text p{margin-bottom:18px}
.services{top:1137px;left:0;width:1200px;height:564px;background:linear-gradient(180deg,#2f3338,#1d2126 70%,#2a2e33)}
.service{width:260px;text-align:center;color:var(--white)}
.service .pic{width:222px;height:222px;border-radius:50%;border:8px solid #6d7178;margin:0 auto}
.service h3{font-size:16px;font-weight:700;margin-top:28px;letter-spacing:.3px}
.service p{font-size:14px;line-height:21px;margin-top:10px}
.service .more{color:var(--sky);font-size:11px;font-weight:600;margin-top:14px}
.mission{top:1833px;left:0;width:1200px;text-align:center;font-size:14.5px;line-height:22px;color:#444;padding:0 92px}
.mission h4{font-weight:400;font-size:14.5px}
.quote{top:2085px;left:0;width:1200px;height:494px;background:var(--brand)}
.quote h2{position:absolute;top:40px;width:1200px;text-align:center;color:var(--white);font-size:22px;font-weight:700}
.quote .sub{position:absolute;top:100px;width:1200px;text-align:center;color:var(--white);font-size:12px;font-weight:600}
.field{height:47px;background:var(--sky);color:var(--mist);font-size:13px;padding:14px 24px;top:167px}
.message{left:92px;top:242px;width:1014px;height:141px;background:var(--sky);color:var(--mist);font-size:13px;padding:24px}
.btn-quote{left:530px;top:416px;width:138px;height:35px;background:var(--green);color:var(--white);border-radius:18px;font-size:12px;font-weight:700;text-align:center;line-height:35px}
.why h2{left:97px;top:2622px;font-size:27px;font-weight:600;color:#222}
.why .bar{left:97px;top:2672px;width:40px;height:4px;background:var(--bright)}
.acc{left:97px;width:580px;height:37px;font-size:12px;font-weight:600;color:#222;padding:0 16px;display:flex;justify-content:space-between;align-items:center}
.acc.open{top:2719px;background:#e9e9e9}
.acc.line{border-bottom:1px solid #ddd}
.why-photo{left:97px;top:2784px;width:239px;height:201px;background:linear-gradient(135deg,#8fa1b3,#d6d9dc 55%,#b89060)}
.why-text{left:351px;top:2780px;width:320px;font-size:13px;line-height:22px;color:#444}
.why-text strong{display:block;font-size:14px;color:#222;margin-bottom:10px}
.courier{left:726px;top:2625px;width:387px;height:520px;background:linear-gradient(180deg,#f4f1ec,#d8c3a0 55%,#c59c66)}
.cta-left{top:3169px;left:0;width:605px;height:126px;background:var(--navy);color:var(--white)}
.cta-right{top:3169px;left:605px;width:595px;height:126px;background:var(--bright);color:var(--white)}
.cta-left .q{position:absolute;left:102px;top:28px;font-size:22px;font-weight:300}
.cta-left .phones{position:absolute;left:102px;top:74px;font-size:21px;display:flex;gap:36px}
.cta-left .phones span{display:flex;align-items:center;gap:10px}
.cta-right .r{position:absolute;left:40px;top:46px;font-size:21px;font-weight:300}
.cta-right .btn{position:absolute;left:346px;top:44px;width:146px;height:37px;background:#1f1f1f;border-radius:4px;font-size:15px;text-align:center;line-height:37px}
.footer{top:3295px;left:0;width:1200px;height:290px;background:var(--dark);color:#ddd}
.fcol{top:28px}
.fcol h5{font-size:19px;font-weight:400;color:var(--white)}
.fcol .ul{width:40px;height:4px;background:var(--bright);margin:10px 0 22px}
.fcol ul{list-style:none;font-size:12.5px;line-height:26px}
.fcol p{font-size:12px;line-height:20px}
.fsocial{left:97px;top:258px;display:flex;gap:12px}
.fsocial .dot{width:11px;height:11px;opacity:.7}
.copyright{top:3585px;left:0;width:1200px;height:44px;background:var(--black);color:#ccc;font-size:12px;text-align:center;line-height:44px}
</style>
</head>
<body>

<div class="abs topbar">
  <div class="abs contact">
    <span><svg width="13" height="13" viewBox="0 0 24 24"><path fill="#fff" d="M6.6 10.8a15 15 0 0 0 6.6 6.6l2.2-2.2c.3-.3.7-.4 1-.2 1.1.4 2.3.6 3.6.6.6 0 1 .4 1 1V20c0 .6-.4 1-1 1A17 17 0 0 1 3 4c0-.6.4-1 1-1h3.5c.6 0 1 .4 1 1 0 1.3.2 2.5.6 3.6.1.3 0 .7-.2 1z"/></svg>312.555.0148</span>
    <span><svg width="14" height="11" viewBox="0 0 14 11"><rect x=".5" y=".5" width="13" height="10" fill="none" stroke="#fff"/><path d="M.5 .5 7 6l6.5-5.5" fill="none" stroke="#fff"/></svg>rates@brightlanefreight.com</span>
  </div>
  <div class="abs social"><i class="dot"></i><i class="dot"></i><i class="dot"></i><i class="dot"></i><i class="dot"></i><i class="dot"></i></div>
  <div class="abs login">LOGIN</div>
</div>

<header class="abs header">
  <div class="abs logo"><i></i>Brightlane Freight</div>
  <nav class="abs nav"><span>WHAT WE DO</span><span>HOW WE DO IT</span><span>WHO WE ARE</span><span>TRACKING</span><span>CHAT</span><span>CONTACT</span></nav>
</header>

<div class="abs hero" role="img" aria-label="Container port with stacked shipping containers and cranes under a cloudy sky"></div>

<h2 class="abs title" style="top:760px">WELCOME FROM OUR FOUNDER</h2>
<svg class="abs divider" style="top:808px" viewBox="0 0 60 10"><line x1="0" y1="5" x2="24" y2="5" stroke="#999"/><line x1="36" y1="5" x2="60" y2="5" stroke="#999"/><circle cx="30" cy="5" r="2.5" fill="#999"/></svg>
<div class="abs founder-photo" role="img" aria-label="Portrait of the company founder"></div>
<div class="abs founder-text">
  <p>Brightlane Freight welcomes you to our growing family of clients! We have over 26 years of experience in helping people solve their logistics needs from coast-to-coast. We also provide friendly, exceptional service that makes it easy to do business with us. Give us a call today and experience the difference for yourself!</p>
  <p>“Our service commitment begins from the moment you contact us. We appreciate your trust, and we go the extra mile to ensure that your freight is handled with care and expediency. If an issue comes up, we work tirelessly to resolve it, staying in contact with you until your freight is delivered without issue!”</p>
  <p>Let us take the worry out of your logistics. Relax, we’ve got this! - Marian Holt, Founder</p>
</div>

<section class="abs services" role="region" aria-label="Services">
  <div class="abs service" style="left:51px;top:66px"><div class="pic" role="img" aria-label="Container ship at a port" style="background:linear-gradient(180deg,#9cc3e6,#6a8fb0 50%,#b5523a)"></div><h3>FREIGHT MANAGEMENT</h3><p>We strive for a perfect delivery and promise to be there for anything you may need, every step of the way. Click here to find out more about Freight Management and how we do it.</p><div class="more">READ MORE →</div></div>
  <div class="abs service" style="left:330px;top:66px"><div class="pic" role="img" aria-label="Truck on a highway" style="background:linear-gradient(180deg,#5f9ad8,#cfe0f0 55%,#4a6fa8)"></div><h3>TRANSPORTATION</h3><p>We strive for a perfect delivery and promise to be there for anything you may need, every step of the way. Click here to find out more about Freight Management and how we do it.</p><div class="more">READ MORE →</div></div>
  <div class="abs service" style="left:608px;top:66px"><div class="pic" role="img" aria-label="Warehouse interior with shelving" style="background:linear-gradient(180deg,#f2c35a,#c98a2e 55%,#7a5a2a)"></div><h3>WAREHOUSE &amp; DISTRIBUTION</h3><p>We strive for a perfect delivery and promise to be there for anything you may need, every step of the way. Click here to find out more about Freight Management and how we do it.</p><div class="more">READ MORE →</div></div>
  <div class="abs service" style="left:886px;top:66px"><div class="pic" role="img" aria-label="Port cranes at dusk" style="background:linear-gradient(180deg,#a6c3de,#e7d8c0 55%,#3a3c44)"></div><h3>CARRIERS</h3><p>We strive for a perfect delivery and promise to be there for anything you may need, every step of the way. Click here to find out more about Freight Management and how we do it.</p><div class="more">READ MORE →</div></div>
</section>

<h2 class="abs title" style="top:1741px">WELCOME FROM OUR FOUNDER</h2>
<svg class="abs divider" style="top:1789px" viewBox="0 0 60 10"><line x1="0" y1="5" x2="24" y2="5" stroke="#999"/><line x1="36" y1="5" x2="60" y2="5" stroke="#999"/><circle cx="30" cy="5" r="2.5" fill="#999"/></svg>
<div class="abs mission">
  <h4>Brightlane Vision</h4>
  <p>Brightlane vision is to be the premier third party logistics solution in North America. We will become premier by providing superior customer service, efficient and cost effective warehousing and distribution solutions. The decisions we make today for hiring, training, technology, strategic services and customer satisfaction are based on this vision.</p>
  <h4 style="margin-top:22px">Brightlane Mission</h4>
  <p>Brightlane’s mission is to provide the most thorough and satisfying third-party logistics experience for its customers. Brightlane uses leading technologies and an industry experienced staff to deliver an unparalleled customer service experience. Brightlane leverages the most efficient mode of transportation, and tailors cost effective solutions for warehousing and distribution of your products in every situation.</p>
</div>

<section class="abs quote" aria-label="Request a quote">
  <h2>REQUEST A QUOTE</h2>
  <svg class="abs" style="left:588px;top:80px" width="24" height="14" viewBox="0 0 24 14"><rect x="0" y="1" width="14" height="9" fill="#fff"/><path d="M14 4h5l4 3v3h-9z" fill="#fff"/><circle cx="5" cy="11.5" r="2" fill="#fff"/><circle cx="18" cy="11.5" r="2" fill="#fff"/></svg>
  <div class="sub">We have wide network of offices in all major locations to help you.</div>
  <div class="abs field" style="left:92px;width:235px">Location</div>
  <div class="abs field" style="left:351px;width:234px">To Destination</div>
  <div class="abs field" style="left:610px;width:234px">Person / Cargo</div>
  <div class="abs field" style="left:871px;width:235px">E-mail or number</div>
  <div class="abs message">Message</div>
  <div class="abs btn-quote">GET A QUOTE</div>
</section>

<div class="why">
  <h2 class="abs">WHY PEOPLE LIKE US?</h2>
  <div class="abs bar"></div>
  <div class="abs acc open"><span>24X7 CUSTOMER SUPPORT</span><span>-</span></div>
  <div class="abs why-photo" role="img" aria-label="Delivery worker handing over a parcel beside a van"></div>
  <div class="abs why-text"><strong>WELCOME TO LARKWAY</strong>provides the services as per the customer’s own tastes and desires.</div>
  <div class="abs acc line" style="top:3009px"><span>ONE STOP SHOP</span><span>+</span></div>
  <div class="abs acc line" style="top:3050px"><span>COMPETITIVE PRICES</span><span>+</span></div>
  <div class="abs courier" role="img" aria-label="Courier carrying a stack of cardboard boxes"></div>
</div>

<div class="abs cta-left">
  <div class="q">Have a question or need a custom quote?</div>
  <div class="phones">
    <span><svg width="18" height="18" viewBox="0 0 18 18"><rect x="1" y="2" width="16" height="14" rx="2" fill="#fff"/><rect x="4" y="5" width="10" height="3" fill="#0a3c7d"/></svg>312.555.0148</span>
    <span><svg width="18" height="18" viewBox="0 0 24 24"><path fill="#fff" d="M6.6 10.8a15 15 0 0 0 6.6 6.6l2.2-2.2c.3-.3.7-.4 1-.2 1.1.4 2.3.6 3.6.6.6 0 1 .4 1 1V20c0 .6-.4 1-1 1A17 17 0 0 1 3 4c0-.6.4-1 1-1h3.5c.6 0 1 .4 1 1 0 1.3.2 2.5.6 3.6.1.3 0 .7-.2 1z"/></svg>312.555.0149</span>
  </div>
</div>
<div class="abs cta-right"><div class="r">Ready to get started</div><div class="btn">Get A Quote</div></div>

<footer class="abs footer">
  <div class="abs fcol" style="left:97px;width:290px"><h5>About Us</h5><div class="ul"></div><p>Lorem Ipsum is simply dummy text of the printing and typesetting industry. Lorem Ipsum has been the industry's standard dummy text ever since the 1500s, when an unknown printer took a galley of type and scrambled it to make a type specimen book.</p></div>
  <div class="abs fcol" style="left:452px"><h5>Information</h5><div class="ul"></div><ul><li>About us</li><li>Career</li><li>Terms of use</li><li>Privacy policy</li><li>Contact us</li></ul></div>
  <div class="abs fcol" style="left:670px"><h5>Our service</h5><div class="ul"></div><ul><li>Road Freight</li><li>Courier Services</li><li>Carnet Services</li><li>Cross Trade</li><li>Custom Clearance</li><li>Perishable Handling</li></ul></div>
  <div class="abs fcol" style="left:888px"><h5>Contact Us</h5><div class="ul"></div><p>Larkway Express Ltd<br>27 Mill Road,<br>Easton EA4 2QT<br>Ph: 01632960415<br>Mob : 07700900318<br>Email – operations@larkway.example</p></div>
  <div class="abs fsocial"><i class="dot"></i><i class="dot"></i><i class="dot"></i><i class="dot"></i><i class="dot"></i><i class="dot"></i></div>
</footer>
<div class="abs copyright">© 2013 www.brightlanefreight.com All Rights Reserved.</div>

</body>
</html>
```